Brochure Design Project A5 (UK) 64 pages apox Making Money From Financial Trading

I require a website (long sales letter) turned into a A5 booklet for mailing out will will be full colour. You must provide a complete end to end to service, I will provide all the text and photos and you need to layout and design the brochure, resize photos to fit. I see the size being around 64 sides of UK A5 paper
148 x 210mm 5.83 x 8.27

You must be creative with text layout and typography, this is very text heavy over 10,000 words in to total. the website can be seen at www.gildenmarsh-ledger.com however this is NOT the final text but gives you an idea. (I have attached 5 pages of text)

They typical reader is male over 40, it needs to be readable, experience with magazine layouts and advantage

The finished project must be ready to go to print.

So it needs a front and back cover designed - I have attached a sample DVD cover as an idea from one of our products and then the inside pages, designed/set out

We have made the project guaranteed so step up and give me your best designs

Reason: Dear All. The standard of work submitted so far has been very poor and amateurish. We have decided to use another company for the front and back cover, therefore leaving you to concentrate on the text for inside the booklet. If you wish to resubmit some better designs then please go ahead. Thx

Target Market(s)

The typical client is Male, professional, looking make money from the stockmarket. The end user already knows the author

Industry/Entity Type

Financial

Requirements
Must have
• Must have good and creative typography

```html
<!DOCTYPE html>
<html lang="en">
<head>
<meta charset="utf-8">
<title>Mentored by a Trading Multi-Millionaire – Booklet Spreads</title>
<link rel="stylesheet" href="https://fonts.googleapis.com/css2?family=Tinos:ital,wght@0,400;0,700;1,400&family=PT+Sans+Narrow:wght@400;700&family=PT+Sans:wght@400;700&display=swap">
<style>
:root{
  --stage:#ececec;
  --paper:#ffffff;
  --ink:#1d1d1d;
  --muted:#555555;
  --blue:#2f9fe0;
  --blue-deep:#0c3f78;
  --navy:#0a1e3c;
  --gutter:rgba(0,0,0,.16);
}
*{box-sizing:border-box;margin:0;padding:0}
html,body{width:1171px;height:1200px;overflow:hidden}
body{background:radial-gradient(circle at 50% 40%,#f7f7f7,var(--stage));font-family:"Tinos",serif;color:var(--ink)}
.spread{position:absolute;left:204px;width:762px;height:540px;display:flex;box-shadow:0 8px 24px rgba(0,0,0,.22)}
.spread--first{top:40px}
.spread--second{top:620px}
.page{position:relative;width:381px;height:540px;background:var(--paper);padding:36px 32px 30px;overflow:hidden}
.page--verso{background:linear-gradient(to left,var(--gutter),transparent 26px),var(--paper)}
.page--recto{background:linear-gradient(to right,var(--gutter),transparent 26px),var(--paper)}
.page-arcs{position:absolute;inset:0;width:100%;height:100%;pointer-events:none}
.running-head{position:absolute;top:14px;left:32px;right:32px;font:400 9px "PT Sans",sans-serif;color:var(--muted);border-bottom:1px solid var(--blue);padding-bottom:3px;display:flex;gap:6px}
.page--verso .running-head{justify-content:flex-end}
.folio{font-weight:700;color:var(--ink)}
.body-copy{position:relative;font-size:12.5px;line-height:1.42;text-align:left}
.body-copy p{margin-bottom:9px}
.underline{text-decoration:underline}
.callout-band{position:absolute;left:0;right:0;bottom:34px;background:var(--blue);color:#fff;font:700 15px "PT Sans Narrow",sans-serif;text-align:center;padding:9px 40px;line-height:1.25}
.testimonial{display:flex;gap:14px;align-items:flex-start;margin-top:8px}
.portrait{flex:0 0 118px;height:128px;background:linear-gradient(160deg,#2d6fb3,#a9c7e6 60%,#d9c3a4);border:3px solid #fff;box-shadow:0 0 0 1px #ccc}
.quote{font:italic 400 15px/1.35 "Tinos",serif;color:#333}
.quote-mark{font:700 30px/0 "Tinos",serif;vertical-align:-12px;margin-right:2px}
.headline{font:700 22px/1.12 "PT Sans Narrow",sans-serif;color:#222;margin:18px 0 12px}
.intro{font-size:12.5px;line-height:1.4;margin-top:4px}
.mentor-banner{position:relative;margin:14px -32px 12px;height:150px;background:linear-gradient(135deg,#0b2347,#0d4a8a 55%,#1b6fbd);display:flex;align-items:center}
.mentor-banner__flash{position:absolute;left:0;top:40px;width:260px;height:96px;background:var(--blue-deep);transform:skewY(-7deg);opacity:.85}
.mentor-banner__title{position:relative;font:700 18px/1.12 "PT Sans Narrow",sans-serif;color:#fff;padding:18px 24px 0 36px;transform:rotate(-5deg)}
.mentor-banner__title b{font-size:26px}
.crowd{position:absolute;left:0;right:0;bottom:0;height:118px;background:linear-gradient(to bottom,#ffffff,#c9c9c9)}
.salutation{margin-bottom:8px}
</style>
</head>
<body>

<section class="spread spread--first">
  <article class="page page--verso">
    <svg class="page-arcs" viewBox="0 0 381 540" aria-hidden="true">
      <path d="M20 0 Q-10 270 20 540" fill="none" stroke="var(--blue)" stroke-width="1"/>
      <path d="M360 0 Q395 270 360 540" fill="none" stroke="var(--blue)" stroke-width="1"/>
    </svg>
    <div class="running-head">Mentored by a Trading Multi-Millionaire <span class="folio">| 33</span></div>
    <div class="body-copy">
      <p>I have no dress code; most days I wear no shoes. I don't do meetings. I don't speak to anyone I don't want to, I have no red tape or have to deal with bureaucrats and I don't have to do business with people if I don't like them.</p>
      <p>From the outside you may say I am a social and academic drop out, yet my average earnings are over £24,900 per week. In case you're wondering, that adds up to over £1.2 million a year, regardless of whether the market is booming or crashing. Take for example September 2008.</p>
      <p>September 2008 was a month that decimated the global financial markets. It was the month that US Investment bank Halden Brothers filed for bankruptcy… it was the month US mortgage lenders Farrow Mae and Fenwick Mac were "shored up" by the US government… it was the month many "professional" financial traders literally "lost their shirt"… and…</p>
    </div>
    <div class="callout-band">It Was Also The Month I Banked A Tax-Free Profit Of £314,377.81</div>
  </article>

  <article class="page page--recto">
    <svg class="page-arcs" viewBox="0 0 381 540" aria-hidden="true">
      <path d="M24 0 Q-8 270 24 540" fill="none" stroke="var(--blue)" stroke-width="1"/>
      <path d="M330 0 Q400 270 340 540" fill="none" stroke="var(--blue)" stroke-width="1"/>
    </svg>
    <div class="running-head"><span class="folio">34 |</span> Mentored by a Trading Multi-Millionaire</div>
    <div class="testimonial">
      <div class="portrait" role="img" aria-label="Portrait photograph of Harlan Pryce"></div>
      <p class="quote"><span class="quote-mark">“</span>I cannot do what Miles does; he is a shorter term trader, I am a longer term person. But if you combine what he does and I do then my goodness, you will become extremely successful and one day we will come and work for you<span class="quote-mark">”</span></p>
    </div>
    <h2 class="headline">Harlan Pryce co founder of Meridian Fund with Victor Ashdale and Pryce Raw Materials Index.</h2>
    <div class="body-copy">
      <p>By the way, you don't have to be based in the UK to do this (I am not based there, although I have stated my earnings in pounds), you can easily be earning in Euros, US$, Australian Dollars or South African Rand wherever you happen to live.</p>
    </div>
  </article>
</section>

<section class="spread spread--second">
  <article class="page page--verso">
    <svg class="page-arcs" viewBox="0 0 381 540" aria-hidden="true">
      <path d="M22 0 Q-12 270 22 540" fill="none" stroke="var(--blue)" stroke-width="1"/>
    </svg>
    <div class="running-head">Mentored by a Trading Multi-Millionaire <span class="folio">| 01</span></div>
    <p class="intro">Mentored by a Trading Multi-Millionaire – your limited chance to trade alongside Miles Harrow for the next 12 months and learn as you earn</p>
    <div class="mentor-banner">
      <div class="mentor-banner__flash"></div>
      <h1 class="mentor-banner__title"><b>Only47</b> Apprentice Traders Will Be Privately Mentored By Multi Millionaire Financial Trader Miles Harrow...</h1>
    </div>
    <p class="intro">And those select 47 new members will soon be making an extra £1,000, £3,000, £5,000 + each week. <strong>The question is – will you be one of them?</strong></p>
    <div class="crowd" role="img" aria-label="Grey silhouettes of a small group of people"></div>
  </article>

  <article class="page page--recto">
    <svg class="page-arcs" viewBox="0 0 381 540" aria-hidden="true">
      <path d="M230 0 Q430 250 300 540" fill="none" stroke="var(--blue)" stroke-width="1"/>
      <path d="M26 0 Q-6 270 26 540" fill="none" stroke="var(--blue)" stroke-width="1"/>
    </svg>
    <div class="running-head"><span class="folio">02 |</span> Mentored by a Trading Multi-Millionaire</div>
    <div class="body-copy">
      <p class="salutation">Dear Reader,</p>
      <p>If you would like to pocket an <span class="underline">extra £1,000, £3,000, £5,000+ each week</span> from the financial markets… even if you have zero trading experience, no knowledge and virtually no time at all… then this letter will show you how you can watch and learn as I trade my personal multi-million pound trading account. I will also reveal why the Kai Loong "Open Hand" principles have revolutionised my trading results and why I consistently make money regardless of the market conditions.</p>
      <p>But first, here's something important you should know…</p>
      <p>Over the last decade I have made a multi-million pound fortune by trading and investing in financial markets. This has all been well documented. I employ no staff, have no offices, no specialist equipment and I "work", if that's the right word, from anywhere I choose and on most days I spend less than 30 minutes a day.</p>
    </div>
  </article>
</section>

</body>
</html>
```